Business Card Design for general contractor or developer

General Contractors. We build new buildings as well as redesign and/or remodel existing buildings. Mostly residential, but we want to expand to commercial as well, so we want the design not to be residential specific.We want the design to be modern, but necessarily minimalistic. A monogram type is also a consideration, but would like to see all ideas.

Target Market(s)

Real estate investors, homeowners, future homeowners, commercial building owners

Industry/Entity Type

Contractor

Contact Information for Business Card

BRIMCOVE Developers Corp, 2917 NE 88th Avenue Suite 412 Coral Springs, FL 33071, Darren Kopec, (305) 555-0148, darren@brimcovedev.example

Font styles to use
Other font styles liked:
• Modern type font

Requirements
Must have
• Must be modern looking
Nice to have
• Metallic type or a standout feature
Should not have
• Tools, floorplans

```html
<!DOCTYPE html>
<html lang="en">
<head>
<meta charset="utf-8">
<title>BRIMCOVE Developers Corp – Business Card</title>
<link rel="stylesheet" href="https://fonts.googleapis.com/css2?family=PT+Sans:wght@400;700&family=Cormorant+SC:wght@500&display=swap">
<style>
  :root {
    --page: #e4e5e6;
    --card-grey: #7b7b7b;
    --card-white: #ffffff;
    --forest: #163f30;
    --ink: #1d2a24;
    --name-grey: #555555;
    --wave-grey: #9a9a9a;
    --wave-light: #cfcfcf;
    --paper-text: #ffffff;
  }
  * { box-sizing: border-box; margin: 0; padding: 0; }
  html, body { width: 1200px; height: 907px; overflow: hidden; }
  body {
    background: var(--page);
    font-family: "PT Sans", Arial, sans-serif;
    position: relative;
  }
  .card {
    position: absolute;
    top: 293px;
    width: 520px;
    height: 320px;
    border-radius: 26px;
    overflow: hidden;
    box-shadow: 0 6px 18px rgba(0,0,0,0.18);
  }
  /* Back side */
  .card-back {
    left: 60px;
    background: var(--card-grey);
    color: var(--paper-text);
  }
  .back-brand {
    position: absolute;
    left: 0; right: 0; top: 110px;
    display: flex;
    align-items: center;
    justify-content: center;
    gap: 14px;
    font-weight: 700;
    font-size: 34px;
    letter-spacing: 2px;
  }
  .brand-square {
    width: 26px; height: 26px;
    background: var(--paper-text);
  }
  .back-web {
    position: absolute;
    left: 0; right: 0; bottom: 58px;
    text-align: center;
    font-size: 19px;
    letter-spacing: 3px;
  }
  /* Front side */
  .card-front {
    left: 620px;
    background: var(--card-white);
  }
  .front-wave { position: absolute; inset: 0; }
  .front-brand {
    position: absolute;
    left: 40px; top: 52px;
    display: flex;
    align-items: center;
    gap: 10px;
    color: var(--ink);
  }
  .front-brand .brand-square {
    width: 18px; height: 18px;
    background: var(--forest);
  }
  .front-brand-name {
    font-weight: 700;
    font-size: 17px;
  }
  .holder {
    position: absolute;
    left: 68px; top: 82px;
    font-family: "Cormorant SC", Georgia, serif;
    font-weight: 500;
    font-size: 24px;
    color: var(--name-grey);
    letter-spacing: 0.5px;
  }
  .holder-title { font-size: 18px; }
  .address {
    position: absolute;
    right: 22px; top: 30px;
    text-align: right;
    color: var(--paper-text);
    font-size: 13.5px;
    line-height: 1.45;
  }
  .contacts {
    position: absolute;
    left: 24px; bottom: 14px;
    list-style: none;
    color: var(--paper-text);
    font-size: 14px;
    line-height: 1.5;
  }
  .contacts li { display: flex; align-items: center; gap: 8px; }
  .contacts svg { width: 12px; height: 12px; flex: none; }
</style>
</head>
<body>

<section class="card card-back" aria-label="Card back">
  <div class="back-brand"><span class="brand-square"></span>BRIMCOVE</div>
  <div class="back-web">www.brimcovedev.example</div>
</section>

<section class="card card-front" aria-label="Card front">
  <svg class="front-wave" viewBox="0 0 520 320" preserveAspectRatio="none" aria-hidden="true">
    <path d="M300,0 C360,150 190,235 0,250" fill="none" stroke="var(--wave-light)" stroke-width="8"/>
    <path d="M315,0 C370,160 200,245 0,260" fill="none" stroke="var(--wave-grey)" stroke-width="3"/>
    <path d="M330,0 C385,170 210,255 0,268 L0,320 L520,320 L520,0 Z" fill="var(--forest)"/>
  </svg>

  <div class="front-brand">
    <span class="brand-square"></span>
    <span class="front-brand-name">BRIMCOVE Developers Corp</span>
  </div>
  <div class="holder">Your Name, <span class="holder-title">Title</span></div>

  <address class="address" style="font-style:normal">
    2917 NE 88th Avenue<br>
    Suite 412 Coral Springs<br>
    FL 33071, Darren Kopec
  </address>

  <ul class="contacts">
    <li>
      <svg viewBox="0 0 12 12" aria-hidden="true"><circle cx="6" cy="6" r="5.2" fill="none" stroke="#fff" stroke-width="1.2"/><path d="M4 3.5 L5 3.5 L5.5 5 L4.8 5.6 Q5.5 7 6.4 7.2 L7 6.5 L8.5 7 L8.5 8 Q6 8.6 4 5 Z" fill="#fff"/></svg>
      (305) 555-0148
    </li>
    <li>
      <svg viewBox="0 0 12 12" aria-hidden="true"><rect x="1" y="2.5" width="10" height="7" fill="none" stroke="#fff" stroke-width="1.2"/><path d="M1 2.5 L6 6.5 L11 2.5" fill="none" stroke="#fff" stroke-width="1.2"/></svg>
      darren@brimcovedev.example
    </li>
  </ul>
</section>

</body>
</html>
```